One-Page Promo flyer for Keynote Speaker Profile

Our CEO speaks at professional conferences and business events. We need to create a one-pager to promote his profile to events companies so they may select him to speak at their professional and industry events. He is a paid speaker so this flyer will be used as a selling tool. Please see the brief document for more details. Key aspects that need to be highlighted: company name, left panel as per the brief document.
Target Market(s)
corporate, business, professionals
Industry/Entity Type
Events

```html
<!DOCTYPE html>
<html lang="en">
<head>
<meta charset="utf-8">
<title>Keynote Speaker Profile – Karim Al Rashed</title>
<link href="https://fonts.googleapis.com/css2?family=Lato:ital,wght@0,400;0,700;0,900;1,400&display=swap" rel="stylesheet">
<style>
:root{
  --navy:#1f3a9a;
  --royal:#2450b8;
  --sky:#7fb3e6;
  --yellow:#fbb82a;
  --ink:#1f1f1f;
  --heading:#1b1b1b;
  --dark-head:#1a2a4a;
  --black:#0d0d0d;
  --rule:#8a8a8a;
  --page-bg:#e9e9e9;
  --white:#ffffff;
}
*{box-sizing:border-box;margin:0;padding:0}
html,body{width:1200px;height:1200px;overflow:hidden;background:var(--page-bg);font-family:'Lato',sans-serif;color:var(--ink)}
.flyer{position:absolute;left:190px;top:20px;width:820px;height:1160px;background:var(--white);overflow:hidden}
.abs{position:absolute}
.stripe{left:0;width:820px;height:25px;background:linear-gradient(90deg,var(--navy) 0%,var(--royal) 45%,var(--sky) 100%)}
.stripe.top{top:0}
.stripe.bottom{top:1135px}
.header-photo{left:0;top:25px;width:820px;height:224px;background:linear-gradient(90deg,#7a6a68 0%,#b9a9a4 35%,#d7cdc8 60%,#8c7e7a 85%,#5a4f4d 100%)}
.name-band{left:0;top:249px;width:820px;height:76px;background:linear-gradient(100deg,var(--navy) 0%,var(--navy) 70%,var(--royal) 78%,var(--sky) 100%)}
.portrait{left:49px;top:80px;width:189px;height:219px;border:2px solid var(--white);background:linear-gradient(160deg,#d9d2cc,#9c8e86);box-shadow:0 1px 4px rgba(0,0,0,.4)}
.emblem{left:265px;top:92px;width:100px;height:128px;border-radius:6px;background:linear-gradient(180deg,#e8b828,#c9962a)}
.speaker-name{left:291px;top:263px;color:var(--white);font-size:19px;font-weight:700;line-height:24px}
.speaker-name em{font-weight:400}
.speaker-office{left:291px;top:290px;color:var(--white);font-size:13.5px;line-height:17px}
.social{top:295px;width:52px;height:52px;border-radius:50%;background:var(--royal);border:3px solid var(--white);color:var(--white);font-size:10px;font-weight:700;display:flex;align-items:center;justify-content:center}
.social.chirp{left:682px;background:#2aa3d6}
.social.linkwork{left:741px}
.left-col{left:0;top:325px;width:265px;height:650px;background:var(--yellow)}
.left-col .black{position:absolute;left:0;top:0;width:265px;height:130px;background:var(--black)}
.cover{left:48px;top:365px;width:189px;height:264px;background:linear-gradient(180deg,#3b3b3b 0%,#8a8075 40%,#d7c9a0 100%);box-shadow:0 2px 6px rgba(0,0,0,.5)}
.award{left:18px;top:660px;width:230px;text-align:center;color:var(--dark-head);font-weight:900;font-size:19.5px;line-height:25px}
.award-rule{left:111px;top:773px;width:62px;height:2px;background:var(--dark-head)}
.left-note{left:18px;top:787px;width:230px;text-align:center;color:var(--dark-head);font-size:13.5px;line-height:19.4px}
.quote{left:18px;top:884px;width:230px;text-align:center;color:var(--dark-head);font-size:13.5px;line-height:19.4px}
.quote b{font-weight:700}
.bio{left:291px;top:364px;width:494px;font-size:13.4px;line-height:19.4px;text-align:justify}
.bio p{margin-bottom:12px}
.rule{left:291px;width:485px;height:1px;background:var(--rule)}
.section-title{left:293px;font-size:26px;line-height:30px;color:var(--heading);font-weight:400;letter-spacing:.2px}
.list{list-style:none;font-size:14.6px;line-height:19.4px;text-transform:uppercase;color:var(--ink)}
.list li{position:relative;padding-left:15px}
.list li::before{content:"";position:absolute;left:1px;top:7px;width:5px;height:5px;border-radius:50%;background:var(--ink)}
.keynote-band{left:0;top:974px;width:820px;height:26px;background:linear-gradient(90deg,var(--sky) 0%,var(--royal) 20%,var(--navy) 100%);color:var(--white);font-weight:900;font-size:18px;text-align:center;line-height:26px;padding-left:60px}
.partners{left:24px;top:1008px;width:772px;height:120px;display:flex;flex-direction:column;justify-content:space-around}
.partner-row{display:flex;justify-content:space-between;align-items:center}
.partner{display:flex;align-items:center;gap:5px;font-size:12.5px;font-weight:700;color:var(--navy);white-space:nowrap}
.partner .dot{width:14px;height:14px;border-radius:50%;background:var(--royal)}
.partner .sq{width:14px;height:14px;background:#d2232a}
.partner.red{color:#d2232a}
.partner.dark{color:#1b1b1b}
.partner.orange{color:#e08a1e}
</style>
</head>
<body>
<main class="flyer">
  <div class="abs stripe top"></div>
  <div class="abs header-photo" role="img" aria-label="Photo of the speaker on stage holding a microphone, soft blurred conference background"></div>
  <div class="abs name-band"></div>
  <div class="abs portrait" role="img" aria-label="Portrait photo of the speaker in traditional white headdress"></div>
  <div class="abs emblem" role="img" aria-label="National emblem"></div>
  <div class="abs speaker-name">Karim Al Rashed, <em>CEO,</em></div>
  <div class="abs speaker-office">The Private Office of Sheikh Hamad Al Noor</div>
  <div class="abs social chirp">Chirp</div>
  <div class="abs social linkwork">Linkwork</div>

  <aside class="abs left-col"><div class="black"></div></aside>
  <div class="abs cover" role="img" aria-label="Business magazine cover featuring the speaker"></div>
  <h2 class="abs award">GULF COMMERCE MAGAZINE BUSINESSMAN OF THE YEAR 2015</h2>
  <div class="abs award-rule"></div>
  <p class="abs left-note">Founded the LAUNCH Entrepreneurship Center to train startups to become successful businesses.</p>
  <p class="abs quote"><b>“The UAE’s leading light when it comes to investment”. –</b><br>Gulf Commerce Magazine</p>

  <section class="abs bio">
    <p>With over 18 years of experience in business within the MENA region, Mr. Al Rashed is a pioneer for his visionary approach, high profile networking, and for concluding large regional projects and investments worth more than 1.06 billion USD.</p>
    <p>He is also the Executive Counselor of Al Sahar Investments &amp; Development, an investment division of Al Sahar Enterprises, a holding group of companies owned by His Highness Sheikh Rashid Al Noor.</p>
    <p>Mr. Al Rashed is also a board member of Meridian Group, an International Private Equity that focuses on emerging markets such as the Middle East, India, and Africa. Mr. Al Rashed is a Bachelor degree holder from Lone Star State University (Cedar Falls, Texas).</p>
  </section>

  <div class="abs rule" style="top:600px"></div>
  <h3 class="abs section-title" style="top:607px">SPEAKING THEMES:</h3>
  <ul class="abs list" style="left:291px;top:646px;width:260px">
    <li>Business &nbsp;in the UAE</li>
    <li>UAE Trade &amp; Regulations</li>
    <li>Investment Management</li>
  </ul>
  <ul class="abs list" style="left:550px;top:646px;width:235px">
    <li>Entrepreneurship</li>
    <li>Networking</li>
    <li>Government &amp; Private<br>Sector &nbsp;Relations</li>
  </ul>
  <div class="abs rule" style="top:734px"></div>
  <h3 class="abs section-title" style="top:752px">SPEAKING ENGAGEMENTS:</h3>
  <ul class="abs list" style="left:291px;top:793px;width:480px">
    <li>Positioning your business in the ME - Understanding<br>regulations and trade opportunities of<br>locating in the UAE</li>
    <li>How to do business with the Arabs in the &nbsp;GCC</li>
    <li>Leveraging the trade and investment<br>opportunities in the U.A.E</li>
    <li>Tendering in Dubai – Winning high value deals and<br>government contracts</li>
  </ul>

  <div class="abs keynote-band">KEYNOTES AND PRESENTATIONS FOR:</div>
  <section class="abs partners">
    <div class="partner-row">
      <div class="partner"><span class="dot"></span>Anglo Trade Circle</div>
      <div class="partner red">Southern Cross Council</div>
      <div class="partner dark">Coastal Daily</div>
      <div class="partner"><span class="dot"></span>Atlantic Gulf Council</div>
      <div class="partner">Harbor Chamber</div>
    </div>
    <div class="partner-row">
      <div class="partner red"><span class="sq"></span>gulfcommerce.net</div>
      <div class="partner dark">Alpine Trade Office</div>
      <div class="partner red">Taste Expo</div>
      <div class="partner"><span class="dot"></span>Prairie Commission</div>
      <div class="partner dark">Savanna Council</div>
      <div class="partner orange">Mesa Data</div>
      <div class="partner orange">Ledger Wire</div>
    </div>
  </section>
  <div class="abs stripe bottom"></div>
</main>
</body>
</html>
```